Letterhead, envelope, business card design

I am looking to update the communication materials for our Association and Foundation. We have two organization (Fenwick Parish Bar Association (the membership organization for lawyers and judges) and the Fenwick Parish Bar Foundation (the charitable arm of our organization).

I am attaching copies of the two organizations logos.

I am looking to update the following pieces:
* our current versions are attached for your review
* the image conveyed should be sophisticated
* Our organization color is reflex blue (I don't think the Foundation logo is correct in the versions I have)

Association:
(1) 8.5" x 11" letterhead (page 1)
(2) #10 envelopes (page 2)
(3) note cards (page 3)
(4) note card envelope (page 4)

Foundation:
(5) 8.5" x 11" letterhead (page 5)
(6) #10 envelopes (page 6)
(7) note cards (page 7)
(8) note card envelope (page 8)

Joint Association and Foundation: (using both logos)
(9) 7.5" x 10.5" (monarch) letterhead (no current version)
(10) Monarch envelope (no current version)
(11) two sided business card (page 9)

FUTURE PROJECTS:
** Membership form (tri-fold 8.5" x 11" )(page 11&12)
** Foundation overview brochure (bi-fold 8.5" x 11") (page13&14)

Target Market(s)

Lawyers and Judges

Industry/Entity Type

Business

Font styles to use
Serif

Requirements
Must have
• Street Address, City, State, Zip, Phone, web address
Nice to have
• .
Should not have
• no clip art, no additional images other than logos

```html
<!DOCTYPE html>
<html lang="en">
<head>
<meta charset="utf-8">
<title>Fenwick Parish Bar Association Stationery</title>
<link href="https://fonts.googleapis.com/css2?family=Arimo:wght@400;700&family=Tinos:wght@400;700&display=swap" rel="stylesheet">
<style>
:root{
  --reflex:#0a58a8;
  --navy:#2b2f80;
  --paper:#ffffff;
  --ink:#1d1d1f;
  --stage:#e4e5e7;
}
*{margin:0;padding:0;box-sizing:border-box}
html,body{width:1189px;height:1200px;overflow:hidden;background:var(--stage)}
body{position:relative;font-family:"Arimo",Arial,sans-serif;color:var(--ink)}
.sheet{position:absolute;background:var(--paper);overflow:hidden;box-shadow:0 1px 3px rgba(0,0,0,.12)}
.wave{position:absolute;left:0;bottom:0;width:100%}
.wave path{fill:var(--reflex)}
.brand{font-family:"Tinos",serif;color:var(--reflex);text-align:center;text-transform:uppercase;letter-spacing:.12em;line-height:1.25;font-weight:400;display:flex;align-items:center;gap:6px;justify-content:center}
.brand .dot{border-radius:50%;background:var(--reflex);flex:none}
.brand.white{color:#fff}
.brand.white .dot{background:#fff}
.footer-line{position:absolute;left:0;width:100%;text-align:center;color:#fff;font-family:"Tinos",serif;line-height:1.45}
.footer-line b{font-family:"Arimo",sans-serif;font-weight:700}

/* Letterhead */
.letterhead{left:59px;top:72px;width:420px;height:542px}
.letterhead .brand{position:absolute;top:36px;left:0;width:100%;font-size:13px}
.recipient{position:absolute;left:33px;top:146px;font-size:7px;line-height:1.35}
.recipient .name{font-size:8px;font-weight:700;margin-bottom:3px}
.body-copy{position:absolute;left:33px;top:213px;width:352px;font-size:7.1px;line-height:12.3px}
.body-copy p+p{margin-top:12px}
.closing{position:absolute;left:33px;top:402px;font-size:7.4px;line-height:1.35}
.signature{display:block;width:96px;height:30px;margin:8px 0 6px;background:linear-gradient(90deg,#2a2a2e22,#2a2a2e10);border-radius:3px}
.closing .name{font-weight:700;font-size:7.8px}

/* Folder */
.folder{left:502px;top:72px;width:418px;height:542px;background:var(--reflex)}
.folder .brand{position:absolute;top:110px;left:0;width:100%;font-size:15px}
.folder .url{position:absolute;bottom:40px;width:100%;text-align:center;color:#fff;font-family:"Tinos",serif;font-size:6.5px}

/* Note cards */
.note-a{left:59px;top:640px;width:315px;height:245px}
.note-b{left:401px;top:640px;width:301px;height:231px}
.note-c{left:724px;top:653px;width:392px;height:196px}
.note-a .brand,.note-c .brand{position:absolute;top:18px;left:14px;font-size:10px;text-align:left}
.note-b .brand{position:absolute;top:14px;left:0;width:100%;font-size:9px}
.note-b .body-copy{left:30px;top:74px;width:240px;font-size:4.9px;line-height:8.4px}
.note-b .body-copy p+p{margin-top:8px}

/* Envelopes */
.envelope{background:var(--paper)}
.flap{position:absolute;top:0;left:0;width:100%}
.flap path{fill:var(--reflex)}
.env-small{left:56px;top:901px;width:315px;height:246px}
.env-small .brand{position:absolute;top:12px;left:0;width:100%;font-size:8px}
.env-large{left:724px;top:949px;width:392px;height:197px}
.env-large .brand{position:absolute;top:13px;left:0;width:100%;font-size:8px}

/* Business card */
.card-front{left:401px;top:904px;width:138px;height:243px;font-family:"Tinos",serif;color:var(--reflex);text-align:center}
.card-front .brand{position:absolute;top:28px;left:0;width:100%;font-size:9px}
.card-name{position:absolute;top:108px;width:100%;font-size:9px;font-weight:700}
.card-title{position:absolute;top:119px;width:100%;font-size:6.3px}
.card-address{position:absolute;top:143px;width:100%;font-size:6.3px;line-height:1.45}
.card-contact{position:absolute;top:164px;width:100%;font-size:6.3px;line-height:1.4}
.card-contact b{font-weight:700}
.card-email{position:absolute;top:199px;width:100%;font-size:6.3px}
.card-front .footer-line{bottom:4px;font-size:6.3px;font-weight:700}
.card-back{left:557px;top:904px;width:140px;height:243px;font-family:"Tinos",serif;color:var(--navy);text-align:center}
.card-back .brand{position:absolute;top:20px;left:0;width:100%;font-size:10px;font-weight:700;color:var(--navy);letter-spacing:.04em}
.card-back .brand .dot{background:var(--navy)}
.headline{position:absolute;top:115px;width:100%;font-size:14px;font-weight:700}
.subline{position:absolute;top:133px;width:100%;font-size:7px;font-weight:700}
.card-url{position:absolute;top:168px;width:100%;font-size:10px}
.hours{position:absolute;top:196px;width:100%;font-size:6.6px;line-height:1.35}
.card-back .band{position:absolute;left:0;bottom:0;width:100%;height:23px;background:var(--navy)}
</style>
</head>
<body>

<section class="sheet letterhead">
  <div class="brand"><span class="dot" style="width:8px;height:8px"></span><span>Fenwick Parish<br>Bar Association</span></div>
  <div class="recipient">
    <div class="name">ALAN PRYCE</div>
    Street Name,City Name.<br>Zip Coad 0000
  </div>
  <div class="body-copy">
    <p>Lorem Ipsum is simply dummy text of the printing and typesetting industry. Lorem Ipsum has been the industry's standard dummy text ever since the 1500s, when an unknown printer took a galley of type and scrambled it to make a type specimen book. It has survived not only five centuries,but also the leap into electronic typesetting, remaining essentially unchanged. It was popularised in the 1960s with the release of Letraset sheets containing Lorem Ipsum passages, and more recently with desktop publishing software like Aldus PageMaker including versions of Lorem Ipsum.</p>
    <p>It is a long established fact that a reader will be distracted by the readable content of a page when looking at its layout. The point of using Lorem Ipsum is that it has a more-or-less normal distribution of letters, as opposed to using 'Content here, content here', making it look like readable English. Many desktop and publishing packages and web page editors now use Lorem Ipsum as their default model text, and a search for 'lorem ipsum' will uncover many web sites still in their infancy. Various versions have evolved over the years, sometimes by accident, sometimes on purpose (injected humour and the like).</p>
  </div>
  <div class="closing">
    Regards,
    <span class="signature" role="img" aria-label="Handwritten signature of Helen Ward"></span>
    <div class="name">Helen Ward</div>
    General Maneger
  </div>
  <svg class="wave" height="64" viewBox="0 0 420 64" preserveAspectRatio="none"><path d="M0,0 Q210,36 420,2 L420,64 L0,64Z"/></svg>
  <div class="footer-line" style="bottom:9px;font-size:6.4px"><b>P:</b> 555.210.4400 | <b>E:</b> info@fenwickbar.org | <b>A:</b> 41 Harbor Street. Suite B Ashford. IL 60091<br><b>W:</b> www.fenwickbar.org</div>
</section>

<section class="sheet folder">
  <div class="brand white"><span class="dot" style="width:9px;height:9px"></span><span>Fenwick Parish<br>Bar Association</span></div>
  <div class="url">www.fenwickbar.org</div>
</section>

<section class="sheet note-a">
  <div class="brand"><span class="dot" style="width:6px;height:6px"></span><span>Fenwick Parish<br>Bar Association</span></div>
  <svg class="wave" height="58" viewBox="0 0 315 58" preserveAspectRatio="none"><path d="M0,0 Q158,34 315,0 L315,58 L0,58Z"/></svg>
  <div class="footer-line" style="bottom:8px;font-size:5px"><b>P:</b> 555.210.4400 | <b>E:</b> info@fenwickbar.org | <b>A:</b> 41 Harbor Street. Suite B Ashford. IL 60091</div>
</section>

<section class="sheet note-b">
  <div class="brand"><span class="dot" style="width:6px;height:6px"></span><span>Fenwick Parish<br>Bar Association</span></div>
  <div class="body-copy">
    <p>Lorem Ipsum is simply dummy text of the printing and typesetting industry. Lorem Ipsum has been the industry's standard dummy text ever since the 1500s, when an unknown printer took a galley of type and scrambled it to make a type specimen book. It has survived not only five centuries,but also the leap into electronic typesetting, remaining essentially unchanged. It was popularised in the 1960s with the release of Letraset sheets containing Lorem Ipsum passages, and more recently with desktop publishing software like Aldus PageMaker including versions of Lorem Ipsum.</p>
    <p>It is a long established fact that a reader will be distracted by the readable content of a page when looking at its layout. The point of using Lorem Ipsum is that it has a more-or-less normal distribution of letters, as opposed to using 'Content here, content here', making it look like readable English. Many desktop and publishing packages and web page editors now use Lorem Ipsum as their default model text, and a search for 'lorem ipsum' will uncover many web sites still in their infancy. Various versions have evolved over the years, sometimes by accident, sometimes on purpose (injected humour and the like).</p>
  </div>
  <svg class="wave" height="47" viewBox="0 0 301 47" preserveAspectRatio="none"><path d="M0,2 Q150,22 301,0 L301,47 L0,47Z"/></svg>
  <div class="footer-line" style="bottom:6px;font-size:5px"><b>P:</b> 555.210.4400 | <b>E:</b> info@fenwickbar.org | <b>A:</b> 41 Harbor Street. Suite B Ashford. IL 60091<br><b>W:</b> www.fenwickbar.org</div>
</section>

<section class="sheet note-c">
  <div class="brand"><span class="dot" style="width:6px;height:6px"></span><span>Fenwick Parish<br>Bar Association</span></div>
  <svg class="wave" height="52" viewBox="0 0 392 52" preserveAspectRatio="none"><path d="M0,0 Q196,36 392,0 L392,52 L0,52Z"/></svg>
  <div class="footer-line" style="bottom:10px;font-size:5.3px"><b>P:</b> 555.210.4400 | <b>E:</b> info@fenwickbar.org | <b>A:</b> 41 Harbor Street. Suite B Ashford. IL 60091</div>
</section>

<section class="sheet envelope env-small">
  <svg class="flap" height="56" viewBox="0 0 315 56" preserveAspectRatio="none"><path d="M0,0 L315,0 L311,52 Q309,56 300,56 L15,56 Q6,56 5,52Z"/></svg>
  <div class="brand white"><span class="dot" style="width:5px;height:5px"></span><span>Fenwick Parish<br>Bar Association</span></div>
</section>

<section class="sheet card-front">
  <div class="brand"><span class="dot" style="width:6px;height:6px"></span><span>Fenwick Parish<br>Bar Association</span></div>
  <div class="card-name">Daniel R. Marsh</div>
  <div class="card-title">Executive Director</div>
  <div class="card-address">41 Harbor Street. Suite B<br>Ashford. IL 60091</div>
  <div class="card-contact"><b>Direct:</b> (555) 210-7100<br><b>Office:</b> (555) 210-4400<br><b>Fax:</b> (555) 210-8259<br><b>Cell:</b> (555) 318-6333</div>
  <div class="card-email"><b>Email:</b> dmarsh@fenwickbar.org</div>
  <svg class="wave" height="24" viewBox="0 0 138 24" preserveAspectRatio="none"><path d="M0,0 Q69,10 138,0 L138,24 L0,24Z"/></svg>
  <div class="footer-line">www.fenwickbar.org</div>
</section>

<section class="sheet card-back">
  <div class="brand"><span class="dot" style="width:6px;height:6px"></span><span>Fenwick Parish<br>Bar Foundation</span></div>
  <div class="headline">Need a lawyer?</div>
  <div class="subline">Don't know who to call?</div>
  <div class="card-url">www.fenwickbar.org</div>
  <div class="hours">Monday- Friday<br>8:00a.m. to 4:30p.m.</div>
  <div class="band"></div>
</section>

<section class="sheet envelope env-large">
  <svg class="flap" height="56" viewBox="0 0 392 56" preserveAspectRatio="none"><path d="M0,0 L392,0 L387,52 Q386,56 376,56 L16,56 Q6,56 5,52Z"/></svg>
  <div class="brand white"><span class="dot" style="width:5px;height:5px"></span><span>Fenwick Parish<br>Bar Association</span></div>
</section>

</body>
</html>
```